New Alcoholic Spiked Seltzer Line

We need a can design for a line of low calorie alcoholic seltzer. This product is a sparkling water and vodka drink with no sugar added in a slim 12 oz can.

This is a lighter, healthier, alternative to the sugary ready-to-drinks on the market. The product contains only 3 ingredients: Vodka, Water and Natural Flavors. It has only 100 calories but still has 5% alcohol, so you don't need to sacrifice alcohol to cut calories.

This product also does not contain any preservatives.

We want this design to communicate the following objectives to the consumer and in this order:

1. Appetizing product
2.Low calorie
3.Communicate the type of beverage (Spiked Seltzer)

The brand name of the product is VELKA.

The flavor of the product needed to be used for the design is Mango-Orange.

Comparable products are:

www.brisavelfizz.example/
https://www.tarnowbubble.example
https://quellrind.example/

The designs should not infringe or copy the creative directions of the products mentionned above. They are only given so that you can better understand the type of product we are developing.

Target Market(s)

Young Professional women between the ages of 25 and 44

Industry/Entity Type

Product

Colors

Designer to choose colors to be used in the design.

Requirements
Must have
• Design extendibility, meaning it can be adapted for other flavors.
• This is a new category in the market we are targeting, so consumers must easily be able to identify what type of product this is.

```html
<!DOCTYPE html>
<html lang="en">
<head>
<meta charset="utf-8">
<title>VELKA Spiked Seltzer – Mango Orange Can</title>
<link rel="stylesheet" href="https://fonts.googleapis.com/css2?family=Montserrat:wght@400;500;600&display=swap">
<style>
  :root {
    --backdrop: #eef1f4;
    --mango: #f5c331;
    --label-white: #ffffff;
    --ink: #2b2b2b;
    --rim-light: #e9ebee;
    --rim-dark: #b9bdc3;
  }
  html, body {
    margin: 0;
    padding: 0;
    width: 1197px;
    height: 1200px;
    overflow: hidden;
    background: var(--backdrop);
  }
  .canvas {
    position: relative;
    width: 1197px;
    height: 1200px;
  }
  .can {
    position: absolute;
    left: 385px;
    top: 48px;
    width: 426px;
    height: 1104px;
  }
  .can text {
    font-family: "Montserrat", sans-serif;
  }
  .brand-word { font-size: 140px; font-weight: 500; }
  .brand-word--on-mango { fill: var(--label-white); }
  .brand-word--on-white { fill: var(--ink); }
  .badge-name { font-size: 34px; font-weight: 500; fill: var(--label-white); letter-spacing: 2px; }
  .category { font-size: 34px; font-weight: 600; fill: var(--ink); letter-spacing: 1px; }
  .flavor { font-size: 44px; font-weight: 600; fill: var(--ink); letter-spacing: 2px; }
  .claim { font-size: 22px; font-weight: 500; fill: var(--ink); }
  .nutrition { font-size: 24px; font-weight: 500; fill: var(--ink); }
</style>
</head>
<body>
<main class="canvas">
  <svg class="can" viewBox="0 0 426 1104" xmlns="http://www.w3.org/2000/svg" role="img" aria-label="VELKA Spiked Seltzer, Mango Orange, 100 calories, 5% alcohol">
    <defs>
      <linearGradient id="rimShade" x1="0" x2="1" y1="0" y2="0">
        <stop offset="0" stop-color="var(--rim-dark)"/>
        <stop offset="0.5" stop-color="var(--rim-light)"/>
        <stop offset="1" stop-color="var(--rim-dark)"/>
      </linearGradient>
      <clipPath id="mangoArea">
        <polygon points="0,28 426,28 426,114 0,774"/>
      </clipPath>
      <clipPath id="whiteArea">
        <polygon points="426,114 426,1044 0,1044 0,774"/>
      </clipPath>
    </defs>

    <!-- lid and base -->
    <rect class="can-lid" x="14" y="0" width="398" height="34" rx="10" fill="url(#rimShade)"/>
    <rect class="can-base" x="14" y="1036" width="398" height="68" rx="18" fill="url(#rimShade)"/>

    <!-- label body -->
    <rect class="label-body" x="0" y="28" width="426" height="1016" rx="6" fill="var(--label-white)"/>
    <polygon class="label-mango-field" points="0,28 426,28 426,114 0,774" fill="var(--mango)"/>

    <!-- brand badge -->
    <circle class="badge-ring" cx="210" cy="248" r="88" fill="none" stroke="var(--label-white)" stroke-width="8"/>
    <text class="badge-name" x="210" y="260" text-anchor="middle">VELKA</text>

    <!-- brand word split across the diagonal -->
    <g clip-path="url(#mangoArea)">
      <text class="brand-word brand-word--on-mango" x="16" y="494" textLength="384" lengthAdjust="spacingAndGlyphs">VELKA</text>
    </g>
    <g clip-path="url(#whiteArea)">
      <text class="brand-word brand-word--on-white" x="16" y="494" textLength="384" lengthAdjust="spacingAndGlyphs">VELKA</text>
    </g>

    <text class="category" x="400" y="568" text-anchor="end">SPIKED SELTZER</text>

    <text class="flavor" x="16" y="734" textLength="384" lengthAdjust="spacingAndGlyphs">MANGO ORANGE</text>

    <text class="claim" x="212" y="964" text-anchor="middle">Appetizing product</text>

    <rect class="nutrition-band" x="0" y="978" width="426" height="40" fill="var(--mango)"/>
    <text class="nutrition" x="213" y="1006" text-anchor="middle">100 cal  /  5%alc.</text>
  </svg>
</main>
</body>
</html>
```